Business Card Design

I already have a company logo for my company. I have a logo for the manufacturer we represent. I want a professional business card design.

```html
<!DOCTYPE html>
<html lang="en">
<head>
<meta charset="utf-8">
<title>Signal Point Solutions – Business Card</title>
<link rel="stylesheet" href="https://fonts.googleapis.com/css2?family=Lato:wght@400;700;900&family=Michroma&display=swap">
<style>
  :root {
    --stage: #d9d9db;
    --card-dark: #1d1d1f;
    --card-mid: #2b2b2e;
    --edge-gold: #e0a81a;
    --brand-red: #e8232b;
    --brand-gold: #e3a516;
    --text-light: #f2f2f2;
    --silver-hi: #f4f4f4;
    --silver-lo: #9a9a9d;
    --band-text: #2a2a2c;
  }
  * { box-sizing: border-box; margin: 0; padding: 0; }
  html, body { width: 1200px; height: 982px; overflow: hidden; }
  body {
    background: var(--stage);
    font-family: "Lato", sans-serif;
    position: relative;
  }
  .card {
    position: absolute;
    left: 220px;
    width: 760px;
    height: 434px;
    border-radius: 22px;
    overflow: hidden;
    border-bottom: 4px solid var(--edge-gold);
    box-shadow: 0 14px 30px rgba(0,0,0,.35);
  }
  .card-front { top: 30px; }
  .card-back  { top: 510px; }
  .card-surface {
    position: absolute; inset: 0;
    background: radial-gradient(ellipse at 40% 35%, var(--card-mid), var(--card-dark) 75%);
  }

  /* Front */
  .brand-lockup {
    position: absolute; left: 0; right: 0; top: 50%;
    transform: translateY(-50%);
    display: flex; align-items: center; justify-content: center; gap: 16px;
  }
  .brand-mark {
    width: 34px; height: 34px; background: var(--brand-red); flex: none;
  }
  .brand-name {
    font-family: "Lato", sans-serif;
    font-weight: 900;
    font-size: 38px;
    letter-spacing: 1px;
    color: var(--text-light);
    white-space: nowrap;
  }

  /* Back */
  .person {
    position: absolute; left: 20px; top: 150px; width: 292px; text-align: right;
  }
  .person-name {
    font-family: "Michroma", sans-serif;
    font-size: 24px;
    color: var(--brand-red);
    letter-spacing: 1px;
    white-space: nowrap;
  }
  .person-title {
    font-size: 21px;
    color: var(--brand-gold);
    margin-top: 6px;
  }
  .divider {
    position: absolute; left: 330px; top: 105px; width: 2px; height: 210px;
    background: linear-gradient(var(--silver-hi), var(--silver-lo) 70%, transparent);
  }
  .contact {
    position: absolute; left: 352px; top: 100px; list-style: none;
    color: var(--text-light); font-size: 19px; line-height: 1.3;
  }
  .contact li { display: flex; gap: 10px; align-items: flex-start; margin-bottom: 4px; }
  .contact svg { width: 16px; height: 16px; fill: var(--brand-red); flex: none; margin-top: 4px; }
  .contact .company { color: var(--brand-red); font-weight: 700; }
  .web-band {
    position: absolute; left: 0; bottom: 40px; width: 510px; height: 50px;
    background: linear-gradient(180deg, var(--silver-hi), var(--silver-lo));
    clip-path: polygon(0 0, 95% 0, 100% 100%, 0 100%);
    display: flex; align-items: center; padding-left: 70px;
    font-size: 18px; letter-spacing: 5px; font-weight: 700; color: var(--band-text);
    white-space: nowrap;
  }
  .back-brand {
    position: absolute; right: 34px; bottom: 55px;
    display: flex; align-items: center; gap: 8px;
  }
  .back-brand .brand-mark { width: 14px; height: 14px; }
  .back-brand .brand-name { font-size: 16px; letter-spacing: .5px; }
</style>
</head>
<body>

<section class="card card-front">
  <div class="card-surface" role="img" aria-label="Dark diamond-plate metal texture"></div>
  <div class="brand-lockup">
    <span class="brand-mark"></span>
    <span class="brand-name">Signal Point Solutions LLC</span>
  </div>
</section>

<section class="card card-back">
  <div class="card-surface" role="img" aria-label="Dark diamond-plate metal texture"></div>

  <div class="person">
    <div class="person-name">DANIEL HART</div>
    <div class="person-title">Founder &amp; CEO</div>
  </div>

  <div class="divider"></div>

  <ul class="contact">
    <li>
      <svg viewBox="0 0 16 16"><path d="M8 0a5.5 5.5 0 0 0-5.5 5.5C2.5 10 8 16 8 16s5.5-6 5.5-10.5A5.5 5.5 0 0 0 8 0zm0 8a2.5 2.5 0 1 1 0-5 2.5 2.5 0 0 1 0 5z"/></svg>
      <span><span class="company">Signal Point Solutions LLC</span><br>423 Street Address Here, City<br>State &amp; ZIP Code Country</span>
    </li>
    <li>
      <svg viewBox="0 0 16 16"><path d="M3.6 1 6 3.8 4.6 5.7a9.5 9.5 0 0 0 5.7 5.7L12.2 10 15 12.4 13.4 15C6.5 14.5 1.5 9.5 1 2.6z"/></svg>
      <span>(123) 456-7890</span>
    </li>
    <li>
      <svg viewBox="0 0 16 16"><path d="M4.5 0h7A1.5 1.5 0 0 1 13 1.5v13a1.5 1.5 0 0 1-1.5 1.5h-7A1.5 1.5 0 0 1 3 14.5v-13A1.5 1.5 0 0 1 4.5 0zM5 2v10h6V2zm3 11a1 1 0 1 0 0 2 1 1 0 0 0 0-2z"/></svg>
      <span>(123) 456-7890</span>
    </li>
    <li>
      <svg viewBox="0 0 16 16"><path d="M4 0h8v4H4zM1 5h14v7h-3v4H4v-4H1zm5 6v3h4v-3z"/></svg>
      <span>(123) 456-7890</span>
    </li>
    <li>
      <svg viewBox="0 0 16 16"><path d="M0 3h16v10H0zm1.5 1.3v.4L8 9l6.5-4.3v-.4z"/></svg>
      <span>info@yourwebsitehere.com</span>
    </li>
  </ul>

  <div class="web-band">WWW.YOURWEBSITEHERE.COM</div>

  <div class="back-brand">
    <span class="brand-mark"></span>
    <span class="brand-name">Signal Point Solutions</span>
  </div>
</section>

</body>
</html>
```